Brochure 11 x 25.5 Trifold

Harborline Staffing Works, Inc. is a payroll, benefits, and HR administration company. We are in need of a brochure to showcase all of our services. Attached is a one-page information sheet that contains the information we want in the brochure as well as several images. The brochure is a 11 x 25.5 tri-fold (a sample is attached). Please use the colors in the attached logo and design to complement our website harborlineworks.example.
Target Market(s)
Company executives
Industry/Entity Type
Human Resource Management
Other font styles liked:
- Avenir LT

```html
<!DOCTYPE html>
<html lang="en">
<head>
<meta charset="utf-8">
<title>Harborline Staffing Works – Trifold Brochure</title>
<link href="https://fonts.googleapis.com/css2?family=Exo+2:wght@500;600;700;800&family=Nunito+Sans:wght@400;600;700&display=swap" rel="stylesheet">
<style>
:root{
  --navy:#0e3a5f;
  --navy-deep:#0a2f4e;
  --green:#8cb63c;
  --lime:#b3d84c;
  --red:#e0452c;
  --orange:#f0a020;
  --olive:#8f9a1e;
  --blue:#2a9ad8;
  --teal:#1aa3a3;
  --ink:#2b2b2b;
  --white:#ffffff;
  --backdrop:#7d7d7d;
}
*{margin:0;padding:0;box-sizing:border-box}
html,body{width:1200px;height:904px;overflow:hidden}
body{background:var(--backdrop);font-family:"Nunito Sans",Arial,sans-serif;color:var(--ink);position:relative}
.spread{position:absolute;left:151px;width:898px;height:387px;background:var(--white);overflow:hidden}
.spread--outside{top:46px}
.spread--inside{top:471px}
.spread > svg.backdrop{position:absolute;left:0;top:0;width:898px;height:387px}
.abs{position:absolute}
.heading{font-family:"Exo 2",Arial,sans-serif;font-weight:700}

/* brand name */
.brand-name{font-family:"Nunito Sans",Arial,sans-serif;font-weight:400;color:var(--navy);letter-spacing:.5px;line-height:1.05;display:flex;align-items:center;gap:6px}
.brand-name .brand-dot{display:inline-block;border-radius:50%;background:var(--green);flex:none}

/* what sets us apart */
.apart-title{left:23px;top:19px;color:var(--white);font-size:11.5px}
.apart-item{width:130px;display:flex;gap:8px;align-items:flex-start}
.apart-icon{width:23px;height:23px;flex:none;margin-top:1px}
.apart-text{font-size:5.9px;line-height:1.3;color:var(--white);text-align:justify}
.apart-text em{font-style:normal;color:var(--lime)}

/* contact */
.contact-title{left:21px;top:286px;font-size:11px;color:var(--navy);font-weight:800}
.contact-line{left:21px;display:flex;align-items:flex-start;gap:6px;font-size:9.2px;color:var(--ink);line-height:1.28}
.contact-icon{width:9px;height:9px;margin-top:2px;flex:none}

/* cover */
.cover-head{left:620px;top:272px;color:var(--white);font-size:17.5px;font-weight:600;line-height:1.33}
.cover-accent{left:620px;top:322px;color:var(--green);font-size:14.5px;font-weight:800}
.cover-url{left:620px;top:355px;color:var(--white);font-size:10.5px}

/* inside left */
.hire-title{left:21px;top:162px;color:var(--navy);font-size:14px;font-weight:800;line-height:1.25;letter-spacing:.2px}
.hire-copy{left:21px;top:203px;width:257px;font-size:6.1px;line-height:1.35;text-align:justify;color:var(--ink)}

/* lifecycle */
.lifecycle{left:322px;top:17px;width:256px;height:151px;border:1px solid var(--green);border-radius:2px}
.life-label{font-size:4.8px;line-height:1.3;color:var(--ink)}
.life-label b{display:block;font-weight:700;font-size:4.9px;letter-spacing:.2px}

/* services */
.services-bar{left:322px;top:176px;width:256px;height:17px}
.services-bar span{position:absolute;left:6px;top:1px;color:var(--white);font-family:"Exo 2",Arial,sans-serif;font-weight:800;font-size:11px}
.service{width:125px}
.service-head{display:flex;gap:6px}
.service-icon{width:25px;height:25px;flex:none;margin-top:1px}
.service-title{font-family:"Exo 2",Arial,sans-serif;font-weight:700;color:var(--navy);font-size:8.4px;line-height:1.15}
.tick-list{list-style:none;margin-top:1px}
.tick-list li{position:relative;padding-left:6px;font-size:5.3px;line-height:1.25;margin-bottom:2.3px;color:var(--ink)}
.tick-list li::before{content:"";position:absolute;left:0;top:1.4px;width:3.8px;height:3.8px;border-radius:50%;background:var(--green)}
.service-body{margin-left:31px}

.save-badge{left:754px;top:226px;width:122px;height:27px;background:var(--green);border-radius:3px;color:var(--white);font-family:"Exo 2",Arial,sans-serif;font-weight:700;font-size:7.1px;line-height:1.3;text-align:center;padding-top:4px;letter-spacing:.2px}
</style>
</head>
<body>

<!-- ===== OUTSIDE SPREAD ===== -->
<section class="spread spread--outside" aria-label="Brochure outside spread">
  <svg class="backdrop" viewBox="0 0 898 387" aria-hidden="true">
    <defs>
      <linearGradient id="warmOffice" x1="0" y1="0" x2="1" y2="1">
        <stop offset="0" stop-color="#9b6a55"/><stop offset=".5" stop-color="#4a4a4f"/><stop offset="1" stop-color="#c9c9cc"/>
      </linearGradient>
      <linearGradient id="greyOffice" x1="0" y1="0" x2="1" y2="1">
        <stop offset="0" stop-color="#cfcfcf"/><stop offset=".5" stop-color="#8d8d8d"/><stop offset="1" stop-color="#e6e6e6"/>
      </linearGradient>
      <linearGradient id="meetingRoom" x1="0" y1="0" x2="1" y2="1">
        <stop offset="0" stop-color="#2d3135"/><stop offset=".5" stop-color="#6b5a4e"/><stop offset="1" stop-color="#c3c7cc"/>
      </linearGradient>
    </defs>
    <!-- panel 1 -->
    <path d="M0 0H299V258Q299 280 277 280H240V387H0Z" fill="var(--navy)"/>
    <path d="M0 300L70 196H203Q240 196 240 233V300" fill="none" stroke="var(--green)" stroke-width="1.8"/>
    <path d="M255 387L299 322V338L267 387Z" fill="var(--green)"/>
    <!-- panel 2 -->
    <path d="M299 0H425L318 205H299Z" fill="var(--navy)"/>
    <path d="M431 0H449L340 205H322Z" fill="var(--green)"/>
    <path d="M516 301L531 301L472 387H456Z" fill="var(--green)"/>
    <path d="M554 258H790Q822 258 810 287L768 387H505Z" fill="var(--navy)"/>
    <!-- panel 3 -->
    <path d="M836 0H898V62Z" fill="var(--navy)"/>
    <path d="M812 0H826L778 70H764Z" fill="var(--green)"/>
    <path d="M705 85Q712 65 740 65H898" fill="none" stroke="var(--green)" stroke-width="1.6"/>
    <path d="M898 235L862 330H800" fill="none" stroke="var(--green)" stroke-width="1.6"/>
    <path d="M776 353H898V387H760Z" fill="var(--green)"/>
  </svg>

  <div class="abs" role="img" aria-label="Photo: two colleagues reviewing work at a laptop in a brick-walled office" style="left:0;top:217px;width:240px;height:170px;background:linear-gradient(135deg,#9b6a55,#4a4a4f 55%,#c9c9cc);clip-path:polygon(0 20%,16% 0,90% 0,100% 14%,100% 100%,0 100%)"></div>
  <div class="abs" role="img" aria-label="Black and white photo: two women working together at a laptop" style="left:348px;top:0;width:250px;height:198px;background:linear-gradient(135deg,#d6d6d6,#8d8d8d 55%,#eeeeee);clip-path:polygon(41% 0,100% 0,100% 100%,0 100%)"></div>
  <div class="abs" role="img" aria-label="Photo: a manager guiding colleagues during a meeting at a conference table" style="left:606px;top:65px;width:292px;height:193px;background:linear-gradient(135deg,#2d3135,#6b5a4e 55%,#c3c7cc);clip-path:polygon(4% 100%,26% 12%,38% 0,100% 0,100% 100%)"></div>

  <!-- panel 1 text -->
  <h2 class="abs heading apart-title">What sets us apart?</h2>
  <div class="abs apart-item" style="left:21px;top:39px">
    <svg class="apart-icon" viewBox="0 0 24 24"><circle cx="12" cy="12" r="10.5" fill="none" stroke="var(--green)" stroke-width="1.6"/><circle cx="12" cy="12" r="7.5" fill="var(--green)" opacity=".25"/><path d="M7 13l3 3 7-7" fill="none" stroke="var(--lime)" stroke-width="1.4"/></svg>
    <p class="apart-text">Our <em>dedicated team of experts</em> is always just a call or email away! You get direct phone numbers to the professionals you need!</p>
  </div>
  <div class="abs apart-item" style="left:156px;top:39px">
    <svg class="apart-icon" viewBox="0 0 24 24"><circle cx="12" cy="12" r="10.5" fill="none" stroke="var(--green)" stroke-width="1.6"/><circle cx="12" cy="12" r="7.5" fill="var(--green)" opacity=".25"/><path d="M7 9h10v3H7zM8 13h8v3H8z" fill="none" stroke="var(--lime)" stroke-width="1.1"/></svg>
    <p class="apart-text">We are equipped with <em>education, experience, certifications and motivation.</em> Our staff executes at the highest level in payroll and HR every day.</p>
  </div>
  <div class="abs apart-item" style="left:21px;top:87px">
    <svg class="apart-icon" viewBox="0 0 24 24"><circle cx="12" cy="12" r="10.5" fill="none" stroke="var(--green)" stroke-width="1.6"/><circle cx="12" cy="12" r="7.5" fill="var(--green)" opacity=".25"/><path d="M7 7h4v4H7zM13 7h4v4h-4zM7 13h4v4H7zM13 13h4v4h-4z" fill="none" stroke="var(--lime)" stroke-width="1.1"/></svg>
    <p class="apart-text">Employee information is automatically integrated acrossall modules, <em>eliminating duplicate data entry and significantly reducing errors.</em></p>
  </div>
  <div class="abs apart-item" style="left:156px;top:87px">
    <svg class="apart-icon" viewBox="0 0 24 24"><circle cx="12" cy="12" r="10.5" fill="none" stroke="var(--green)" stroke-width="1.6"/><circle cx="12" cy="12" r="7.5" fill="var(--green)" opacity=".25"/><rect x="7" y="6" width="9" height="11" fill="none" stroke="var(--lime)" stroke-width="1.1"/><circle cx="15" cy="15" r="2.5" fill="none" stroke="var(--lime)" stroke-width="1.1"/></svg>
    <p class="apart-text"><em>Access your employee information how you need it when you need it</em> with our quick-access reports and intuitive report writer. We even provide custom reports!</p>
  </div>
  <div class="abs apart-item" style="left:22px;top:137px">
    <svg class="apart-icon" viewBox="0 0 24 24"><circle cx="12" cy="12" r="10.5" fill="none" stroke="var(--green)" stroke-width="1.6"/><circle cx="12" cy="12" r="7.5" fill="var(--green)" opacity=".25"/><rect x="6.5" y="7" width="11" height="8" fill="none" stroke="var(--lime)" stroke-width="1.1"/><path d="M10 18h4" stroke="var(--lime)" stroke-width="1.1"/></svg>
    <p class="apart-text">Our <em>advanced software</em> is used to process payroll for over 88,000 companies and 2.2 million employees nation-wide. It makes even the most complex payrolls easy.</p>
  </div>
  <div class="abs apart-item" style="left:156px;top:137px">
    <svg class="apart-icon" viewBox="0 0 24 24"><circle cx="12" cy="12" r="10.5" fill="none" stroke="var(--green)" stroke-width="1.6"/><circle cx="12" cy="12" r="7.5" fill="var(--green)" opacity=".25"/><path d="M7 14a3 3 0 0 1 1-6 4 4 0 0 1 8 1 2.5 2.5 0 0 1 0 5z" fill="none" stroke="var(--lime)" stroke-width="1.1"/></svg>
    <p class="apart-text">Our <em>client branded, cloud-based Employee and Manager portals</em> allow your employees to access their payroll information quicker and more securely than ever before!</p>
  </div>

  <!-- panel 2 text -->
  <div class="abs brand-name" style="left:321px;top:228px;font-size:13.5px"><span class="brand-dot" style="width:13px;height:13px"></span>HARBORLINE STAFFING WORKS</div>
  <h3 class="abs heading contact-title" style="left:321px">CONTACT US</h3>
  <div class="abs contact-line" style="left:321px;top:301px">
    <svg class="contact-icon" viewBox="0 0 10 10"><circle cx="5" cy="5" r="4.6" fill="none" stroke="var(--navy)" stroke-width="1"/><path d="M5 2.2a1.8 1.8 0 0 1 1.8 1.8C6.8 5.4 5 7.6 5 7.6S3.2 5.4 3.2 4A1.8 1.8 0 0 1 5 2.2z" fill="var(--navy)"/></svg>
    <span>412 Pier Street<br>Harbor City, ST 00000</span>
  </div>
  <div class="abs contact-line" style="left:321px;top:329px">
    <svg class="contact-icon" viewBox="0 0 10 10"><circle cx="5" cy="5" r="5" fill="var(--navy)"/><path d="M3 2.6l1 1.2-.5.8a4 4 0 0 0 1.9 1.9l.8-.5 1.2 1-.6.9C4.9 7.8 2.2 5.1 2.1 3.2z" fill="var(--white)"/></svg>
    <span>555-010-3000</span>
  </div>
  <div class="abs contact-line" style="left:321px;top:343px">
    <svg class="contact-icon" viewBox="0 0 10 10"><circle cx="5" cy="5" r="5" fill="var(--navy)"/><rect x="2.4" y="3.2" width="5.2" height="3.6" fill="none" stroke="var(--white)" stroke-width=".8"/><path d="M2.4 3.2L5 5.3 7.6 3.2" fill="none" stroke="var(--white)" stroke-width=".8"/></svg>
    <span>info@harborlineworks.example</span>
  </div>
  <div class="abs contact-line" style="left:321px;top:357px">
    <svg class="contact-icon" viewBox="0 0 10 10"><circle cx="5" cy="5" r="5" fill="var(--navy)"/><circle cx="5" cy="5" r="3" fill="none" stroke="var(--white)" stroke-width=".7"/><path d="M2 5h6M5 2c-1.5 2-1.5 4 0 6M5 2c1.5 2 1.5 4 0 6" fill="none" stroke="var(--white)" stroke-width=".6"/></svg>
    <span>www.harborlineworks.example</span>
  </div>

  <!-- panel 3 text -->
  <div class="abs brand-name" style="left:622px;top:19px;font-size:13.5px"><span class="brand-dot" style="width:13px;height:13px"></span>HARBORLINE STAFFING WORKS</div>
  <p class="abs heading cover-head">Your single-source<br>solution for the</p>
  <p class="abs heading cover-accent">ENTIRE EMPLOYEE</p>
  <p class="abs cover-url">www.harborlineworks.example</p>
</section>

<!-- ===== INSIDE SPREAD ===== -->
<section class="spread spread--inside" aria-label="Brochure inside spread">
  <svg class="backdrop" viewBox="0 0 898 387" aria-hidden="true">
    <path d="M298 0H318L244 150H224Z" fill="var(--green)"/>
    <path d="M207 387V346Q207 331 222 331H262Q278 331 278 346V387Z" fill="var(--navy)"/>
    <path d="M470 387L500 387L530 340Z" fill="var(--green)" opacity="0"/>
    <path d="M565 387H588L652 297H629Z" fill="var(--green)"/>
    <path d="M598 387H612L668 307H654Z" fill="var(--green)"/>
    <path d="M848 353H898V387H836Z" fill="var(--navy)"/>
    <path d="M840 270Q866 282 855 320L842 360" fill="none" stroke="var(--green)" stroke-width="1.6"/>
  </svg>

  <div class="abs" role="img" aria-label="Photo: a team gathered around a colleague at a laptop in a bright office" style="left:0;top:0;width:298px;height:150px;background:linear-gradient(135deg,#d9dde2,#5d6f86 50%,#e9ecef);clip-path:polygon(0 0,100% 0,75% 100%,0 100%)"></div>
  <div class="abs" role="img" aria-label="Illustration: laptop and phone showing the employee self-service portal" style="left:21px;top:253px;width:208px;height:120px;background:linear-gradient(180deg,#3a3a3a 0,#3a3a3a 4%,#f3f5f7 4%,#e4e8ec 92%,#9aa0a6 92%);border-radius:4px"></div>
  <div class="abs" role="img" aria-label="Photo: business professionals shaking hands in a meeting room" style="left:603px;top:263px;width:262px;height:124px;background:linear-gradient(135deg,#e9eef3,#4c5b6e 55%,#2b3440);clip-path:polygon(18% 0,88% 0,100% 18%,100% 100%,0 100%)"></div>

  <!-- panel 1 text -->
  <h2 class="abs heading hire-title">FROM HIRE TO RETIRE,<br>WE’VE GOT YOU COVERED</h2>
  <p class="abs hire-copy">Harborline Staffing Works has been delivering quality HR and Payroll services for over 25 years. Our dedicated team of professionals is focused on being the best service provider in the industry. Our goal is to relieve business executives of the challenges of managing a dynamic and growing workforce in today’s regulatory environment and give them the freedom to focus on what drives their business.</p>

  <!-- lifecycle -->
  <div class="abs lifecycle"></div>
  <svg class="abs" style="left:0;top:0" width="898" height="387" viewBox="0 0 898 387" aria-label="Employee lifecycle diagram">
    <g fill="none" stroke-width="7">
      <path d="M434.5 72.6A27 27 0 0 1 461.5 72.6" stroke="var(--orange)"/>
      <path d="M461.5 72.6A27 27 0 0 1 475 96" stroke="var(--olive)"/>
      <path d="M475 96A27 27 0 0 1 461.5 119.4" stroke="var(--blue)"/>
      <path d="M461.5 119.4A27 27 0 0 1 434.5 119.4" stroke="var(--teal)"/>
      <path d="M434.5 119.4A27 27 0 0 1 421 96" stroke="var(--navy)"/>
      <path d="M421 96A27 27 0 0 1 434.5 72.6" stroke="var(--red)"/>
    </g>
    <circle cx="448" cy="96" r="21" fill="#e8e8e8"/>
    <text x="448" y="94" text-anchor="middle" font-family="Exo 2, sans-serif" font-size="6.4" fill="var(--navy)">EMPLOYEE</text>
    <text x="448" y="102" text-anchor="middle" font-family="Exo 2, sans-serif" font-weight="700" font-size="6.4" fill="var(--navy)">LIFECYCLE</text>
    <g stroke-width="2" fill="var(--white)">
      <circle cx="418" cy="40" r="13" stroke="var(--red)"/>
      <circle cx="478" cy="40" r="13" stroke="var(--orange)"/>
      <circle cx="507" cy="90" r="13" stroke="var(--olive)"/>
      <circle cx="478" cy="141" r="13" stroke="var(--blue)"/>
      <circle cx="418" cy="141" r="13" stroke="var(--teal)"/>
      <circle cx="389" cy="90" r="13" stroke="var(--navy)"/>
    </g>
    <g fill="none" stroke-width="1.1">
      <path d="M415 36l-3 4 3 4M421 36l3 4-3 4" stroke="var(--red)"/>
      <rect x="473" y="35" width="9" height="10" stroke="var(--orange)"/>
      <circle cx="507" cy="90" r="5" stroke="var(--olive)"/>
      <path d="M473 138h10v7h-10zM473 138l5 4 5-4" stroke="var(--blue)"/>
      <circle cx="418" cy="141" r="5" stroke="var(--teal)"/>
      <circle cx="389" cy="90" r="6" stroke="var(--navy)"/>
    </g>
  </svg>
  <p class="abs life-label" style="left:328px;top:20px;width:70px"><b style="color:var(--red)">SEPARATION</b>COBRA, Retirement plan assistance, DOL Notining</p>
  <p class="abs life-label" style="left:503px;top:20px;width:70px"><b style="color:var(--orange)">HIRING</b>Integrated cloud-based ATS, Auto post to job boards, applicant management and screening</p>
  <p class="abs life-label" style="left:328px;top:59px;width:56px"><b style="color:var(--navy)">EMPLOYEE MANAGEMENT</b>Culture development, discipline, leave management Workers’ Compensation claims, employee verifications handbook</p>
  <p class="abs life-label" style="left:527px;top:65px;width:48px"><b style="color:var(--olive)">ONBOARDING</b>Auto generate notice to new-hire, standard and customized forms and acknowledgements</p>
  <p class="abs life-label" style="left:328px;top:131px;width:76px"><b style="color:var(--teal)">BENEFITS</b>Online enrollment, application, benefit reconciliations, eligibility tracking notifications, retirement plan</p>
  <p class="abs life-label" style="left:503px;top:131px;width:72px"><b style="color:var(--blue)">PAYROLL</b>HRIS, Direct deposits, New Hire Reporting, Employee Portal, Year End Reporting</p>

  <!-- services bar -->
  <svg class="abs services-bar" viewBox="0 0 256 17" aria-hidden="true"><path d="M0 0H84L92 15H0Z" fill="var(--navy)"/><path d="M84 0H87L95 15H256V16.2H0V15H92Z" fill="var(--green)"/></svg>
  <div class="abs services-bar"><span>OUR SERVICES</span></div>

  <!-- service blocks -->
  <div class="abs service" style="left:322px;top:196px">
    <div class="service-head">
      <svg class="service-icon" viewBox="0 0 26 26" fill="none" stroke="var(--navy)" stroke-width="1.2"><path d="M3 11l10-7 10 7v12H3z"/><rect x="7" y="6" width="12" height="10"/><circle cx="13" cy="11" r="3"/></svg>
      <div><p class="service-title">Payroll</p>
        <ul class="tick-list">
          <li>Fast, efficient, accurate</li><li>Paper checks or direct deposit</li><li>Easy time file uploads or integrated time clock options</li><li>New hire reporting</li><li>Custom G/L file</li><li>Comprehensive reporting options</li><li>Certified payroll option</li>
        </ul></div>
    </div>
  </div>
  <div class="abs service" style="left:455px;top:196px">
    <div class="service-head">
      <svg class="service-icon" viewBox="0 0 26 26" fill="none" stroke="var(--navy)" stroke-width="1.2"><circle cx="8" cy="7" r="2.5"/><circle cx="13" cy="6" r="2.5"/><circle cx="18" cy="7" r="2.5"/><path d="M4 15q9-6 18 0M3 18h6l5 3h7"/></svg>
      <div><p class="service-title">Human Resource<br>Administration</p>
        <ul class="tick-list" style="width:100px">
          <li>Wage and hour compliance</li><li>Employee handbooks</li><li>Employee discipline and termination consulting</li><li>Performance management</li><li>Workers’ comp claims administration</li><li>Unemployment administration</li><li>Manager training</li>
        </ul></div>
    </div>
  </div>
  <div class="abs service" style="left:322px;top:290px">
    <div class="service-head">
      <svg class="service-icon" viewBox="0 0 26 26" fill="none" stroke="var(--navy)" stroke-width="1.2"><circle cx="14" cy="9" r="5"/><path d="M14 6v6M3 17l6-1 6 3 7-4M3 22h8l10-4"/></svg>
      <div><p class="service-title">Benefits Management</p>
        <ul class="tick-list">
          <li>Customized benefits packet</li><li>Track new hire eligibility</li><li>Open enrollment assistance</li><li>Electronic enrollment</li><li>Track and submit enrollments</li><li>Provide 401k census report</li><li>Remit retirement plan reports and funds</li><li>ACA compliance</li>
        </ul></div>
    </div>
  </div>
  <div class="abs service" style="left:455px;top:290px">
    <div class="service-head">
      <svg class="service-icon" viewBox="0 0 26 26" fill="none" stroke="var(--navy)" stroke-width="1.2"><circle cx="15" cy="13" r="8"/><path d="M15 8v5l3 2M2 10h5M1 13h5M2 16h5"/></svg>
      <div><p class="service-title">Time and Attendance</p>
        <ul class="tick-list" style="width:100px">
          <li>Integrated with payroll (no double entry)</li><li>Mobile and geofencing options</li><li>Overtime notices</li><li>Online time-off requests</li><li>Swipe and proximity card clocks</li><li>Biometric clocks</li><li>PTO tracking</li>
        </ul></div>
    </div>
  </div>

  <!-- panel 3 services -->
  <div class="abs service" style="left:619px;top:17px;width:135px">
    <div class="service-head">
      <svg class="service-icon" viewBox="0 0 26 26" fill="none" stroke="var(--navy)" stroke-width="1.2"><rect x="3" y="3" width="15" height="20"/><path d="M6 8h9M6 12h9M6 16h6M22 6l-7 12-1 3 3-2 7-12z"/></svg>
      <div><p class="service-title">Employee Onboarding</p>
        <ul class="tick-list">
          <li>Simple, accurate, paperless</li><li>Custom forms and acknowledgements</li><li>Standard forms (W-4, I-9, State withholding, etc)</li><li>Paperless, electronic signatures</li><li>Employee handbook and policy acknowledgements</li><li>Custom welcome videos</li>
        </ul></div>
    </div>
  </div>
  <div class="abs service" style="left:753px;top:17px;width:135px">
    <div class="service-head">
      <svg class="service-icon" viewBox="0 0 26 26" fill="none" stroke="var(--navy)" stroke-width="1.2"><circle cx="13" cy="6" r="2.5"/><circle cx="8" cy="9" r="2"/><circle cx="18" cy="9" r="2"/><path d="M3 12v6l5 5M23 12v6l-5 5M9 15h8"/></svg>
      <div><p class="service-title">Talent Acquisition</p>
        <ul class="tick-list">
          <li>Custom careers page</li><li>Standard or custom job applications</li><li>Easy conversion of applicant data to employee data</li><li>Review, rate &amp; contact applicants</li><li>Mobile-friendly access</li><li>Easy posting to top job boards</li><li>Candidate screening</li>
        </ul></div>
    </div>
  </div>
  <div class="abs service" style="left:619px;top:112px;width:135px">
    <div class="service-head">
      <svg class="service-icon" viewBox="0 0 26 26" fill="none" stroke="var(--navy)" stroke-width="1.2"><path d="M3 11l10-7 10 7v12H3z"/><path d="M3 11l10 7 10-7"/><path d="M13 7l1 2 2 .3-1.5 1.4.4 2.2L13 12l-1.9.9.4-2.2L10 9.3 12 9z"/></svg>
      <div><p class="service-title">COBRA Administration</p>
        <ul class="tick-list">
          <li>Initial notices</li><li>Open enrollment notices</li><li>Easy 24/7 online reporting</li><li>Qualified beneficiary election notices</li><li>Premium collection</li><li>Access to professional advice</li>
        </ul></div>
    </div>
  </div>
  <div class="abs service" style="left:753px;top:112px;width:135px">
    <div class="service-head">
      <svg class="service-icon" viewBox="0 0 26 26" fill="none" stroke="var(--navy)" stroke-width="1.2"><rect x="2" y="9" width="22" height="13" rx="1"/><path d="M5 9l7-6 7 6M5 18h3M10 18h3M15 18h3"/></svg>
      <div><p class="service-title">Cafeteria/FSA/HRA<br>Administration</p>
        <ul class="tick-list">
          <li>Plan documents/materials</li><li>Debit cards</li><li>Easy 24/7 online reporting</li><li>Claims processing</li><li>Plan testing</li>
        </ul></div>
    </div>
  </div>
  <div class="abs service" style="left:619px;top:189px;width:135px">
    <div class="service-head">
      <svg class="service-icon" viewBox="0 0 26 26" fill="none" stroke="var(--navy)" stroke-width="1.2"><path d="M13 3v18M5 6h16M8 22h10M5 6l-3 8h6zM21 6l-3 8h6zM2 14a3 3 0 0 0 6 0M18 14a3 3 0 0 0 6 0"/></svg>
      <div><p class="service-title">Compliance</p>
        <ul class="tick-list">
          <li>Certified experts ensure compliance with all labor laws and regulations</li><li>OSHA Reporting</li><li>Affirmative Action (EEOC)</li><li>Affordable Care Act (ACA)</li><li>Family Medical Leave Act (FMLA)</li><li>Workers’ Comp audits</li>
        </ul></div>
    </div>
  </div>

  <div class="abs brand-name" style="left:757px;top:205px;font-size:8.8px"><span class="brand-dot" style="width:9px;height:9px"></span>HARBORLINE STAFFING WORKS</div>
  <div class="abs save-badge">SAVE TIME AND STAY FOCUSED<br>ON RUNNING YOUR BUSINESS</div>
</section>

</body>
</html>
```